BRV Online

We are a telemedicine based HIV treatment, prevention and hep c clinic looking to help make our online presence known.

Target Market(s)

Future patients. We want to this be informative and have stock images of all different types of people

Industry/Entity Type

Medical

Coding

Coded - Design and coding required

Requirements
Must have
• A Home Page, A page on PrEP, HIV treatment and Hep C. A box in the corner that says book now and a contact us page.

```html
<!DOCTYPE html>
<html lang="en">
<head>
<meta charset="utf-8">
<title>BRV Online – Confidential HIV and Hepatitis C Care</title>
<link href="https://fonts.googleapis.com/css2?family=Righteous&family=Poppins:ital,wght@0,400;0,500;0,600;1,400&display=swap" rel="stylesheet">
<style>
:root{
  --bg:#f6ebe2;
  --white:#ffffff;
  --ink:#161616;
  --muted:#555555;
  --green:#7dc42b;
  --blue:#1b8fd8;
  --dark:#121212;
  --line:#d9d3cd;
  --cream:#f6ecc6;
  --foot-text:#e6e6e6;
}
*{box-sizing:border-box;margin:0;padding:0}
html,body{width:1200px;height:4655px;overflow:hidden}
body{background:var(--bg);font-family:"Poppins",sans-serif;color:var(--ink);position:relative}
.abs{position:absolute}
.display{font-family:"Righteous",sans-serif;font-weight:400}
.photo{position:absolute;overflow:hidden}
.btn{position:absolute;display:flex;align-items:center;justify-content:center;border-radius:30px;color:var(--white);font-size:11px;font-weight:500}
.btn-green{background:var(--green)}
.btn-blue{background:var(--blue)}
.arrow-circle{position:absolute;width:36px;height:36px;border-radius:50%;background:var(--blue);display:flex;align-items:center;justify-content:center}
.pill{position:absolute;left:50%;transform:translateX(-50%);background:var(--white);border-radius:20px;padding:3px 18px;font-size:9px;font-weight:500}
.section-title{position:absolute;left:0;width:1200px;text-align:center;font-size:30px}

/* nav */
.brand{position:absolute;left:94px;top:20px;display:flex;align-items:center;gap:10px;font-family:"Righteous",sans-serif;font-size:22px;color:var(--blue)}
.brand-dot{width:34px;height:34px;border-radius:50%;background:var(--green)}
.nav-links{position:absolute;left:560px;top:30px;display:flex;gap:26px;font-size:10px}

/* hero */
.hero{left:40px;top:81px;width:1120px;height:584px;border-radius:36px;background:linear-gradient(100deg,#f7f5f1 0%,#ece6dc 40%,#d8c2ab 70%,#c9a98a 100%)}
.hero-title{left:94px;top:208px;font-size:48px;line-height:50px}
.hero-sub{left:94px;top:373px;width:380px;font-size:10px;line-height:14px;color:#333}
.social{position:absolute;width:50px;height:50px;border-radius:50%;background:var(--cream);top:572px}

/* services */
.service-card{position:absolute;top:842px;width:224px;height:311px;background:var(--white);border-radius:10px;overflow:hidden;text-align:center}
.service-card .photo{left:0;top:0;width:224px;height:170px}
.icon-badge{position:absolute;width:48px;height:48px;border-radius:50%;background:var(--blue);border:3px solid var(--white);left:88px;top:139px;display:flex;align-items:center;justify-content:center}
.service-card h3{position:absolute;top:196px;width:100%;font-size:14px}
.service-card p{position:absolute;top:218px;left:22px;width:180px;font-size:9px;line-height:13px;color:var(--muted)}
.read-more{position:absolute;top:271px;width:100%;font-size:9px;color:var(--green);text-decoration:underline;font-weight:500}

/* trusted */
.lead{position:absolute;left:0;width:1200px;text-align:center;font-size:10px;line-height:16px;color:#333}
.feature{position:absolute;left:622px;width:453px;height:112px;background:var(--white);border-radius:10px}
.feature .num{position:absolute;left:30px;top:36px;font-size:32px;color:#d8d8d8}
.feature h4{position:absolute;left:90px;top:30px;font-size:13px}
.feature p{position:absolute;left:90px;top:52px;width:330px;font-size:9px;line-height:14px;color:var(--muted)}

/* process */
.process-panel{left:40px;top:1991px;width:1120px;height:626px;background:var(--white);border-radius:34px}
.step{position:absolute;top:2470px;width:257px;text-align:center}
.step .n{font-size:44px;color:var(--green);line-height:52px}
.step .t{font-size:14px;margin-top:4px}
.divider{position:absolute;top:2476px;width:1px;height:108px;background:var(--line)}

/* why */
.why-card{position:absolute;top:2795px;height:318px;background:var(--white);border-radius:8px;overflow:hidden;text-align:center}
.why-card .photo{left:0;top:0;width:100%;height:205px}
.tick{position:absolute;top:3021px;width:38px;height:38px;border-radius:50%;background:var(--blue);display:flex;align-items:center;justify-content:center}
.why-card h3{position:absolute;top:270px;width:100%;font-size:14px}

/* faq */
.faq{position:absolute;left:190px;width:820px;background:var(--white);border-radius:10px;padding:0 24px}
.faq h4{font-size:13px;line-height:44px}
.faq p{font-size:9px;line-height:14px;color:var(--muted);width:700px;margin-top:-6px}
.faq-toggle{position:absolute;right:16px;top:12px;width:20px;height:20px;border-radius:50%;background:var(--green);display:flex;align-items:center;justify-content:center}

/* testimonial */
.quote{left:130px;top:3846px;width:470px;text-align:center;font-size:15px;line-height:25px;font-style:italic;color:#444}

/* footer */
.footer{left:40px;top:4221px;width:1120px;height:434px;background:var(--dark);border-radius:34px 34px 0 0}
.foot-col{position:absolute;top:4412px;color:var(--white)}
.foot-col h5{font-family:"Righteous",sans-serif;font-weight:400;font-size:18px;margin-bottom:4px;color:var(--white)}
.foot-col li{list-style:none;font-size:10px;line-height:22px;color:var(--foot-text)}
</style>
</head>
<body>

<header>
  <div class="brand"><span class="brand-dot"></span>BRV Online</div>
  <nav class="nav-links"><span>Home</span><span>PrEP</span><span>HIV Treatment</span><span>Hep C</span><span>About Us</span><span>Contact Us</span></nav>
  <div class="btn btn-green" style="left:958px;top:22px;width:108px;height:34px">Book Now</div>
  <div class="arrow-circle" style="left:1068px;top:21px"><svg width="16" height="16" viewBox="0 0 16 16"><path d="M3 8h10M9 4l4 4-4 4" stroke="#fff" stroke-width="2" fill="none" stroke-linecap="round"/></svg></div>
</header>

<section>
  <div class="photo hero" role="img" aria-label="Smiling woman with headphones holding a mug at home"></div>
  <h1 class="abs display hero-title">Confidential<br>HIV And Hepatitis C<br>Care Anytime</h1>
  <p class="abs hero-sub">Receive expert, judgment-free care from licensed healthcare providers through secure online consultations. Start treatment, prevention.</p>
  <div class="btn btn-green" style="left:94px;top:417px;width:150px;height:38px">Book Appointment</div>
  <div class="btn btn-blue" style="left:251px;top:417px;width:112px;height:38px">Learn More</div>
  <div class="social" style="left:938px"></div>
  <div class="social" style="left:996px"></div>
  <div class="social" style="left:1054px"></div>
</section>

<section>
  <div class="pill" style="top:754px">Our Service</div>
  <h2 class="section-title display" style="top:782px">Expert Care You Can Trust</h2>
  <article class="service-card" style="left:123px">
    <div class="photo" role="img" aria-label="Lab technician examining a blood sample" style="background:linear-gradient(135deg,#dfe9f2,#a9c6e0)"></div>
    <div class="icon-badge"><svg width="20" height="20" viewBox="0 0 20 20"><circle cx="10" cy="6" r="3" fill="#fff"/><path d="M4 17c0-4 3-6 6-6s6 2 6 6" fill="#fff"/></svg></div>
    <h3 class="display">HIV Treatment</h3>
    <p>Comprehensive treatment plans with ongoing medical support to help you live a healthy life.</p>
    <div class="read-more">Read More</div>
  </article>
  <article class="service-card" style="left:367px">
    <div class="photo" role="img" aria-label="Two young people in masks at a consultation" style="background:linear-gradient(135deg,#c9a27f,#6e5040)"></div>
    <div class="icon-badge"><svg width="20" height="20" viewBox="0 0 20 20"><rect x="3" y="7" width="14" height="6" rx="3" fill="#fff"/></svg></div>
    <h3 class="display">PrEP Prevention</h3>
    <p>Protect yourself from HIV with safe and effective PrEP medication prescribed by experienced.</p>
    <div class="read-more">Read More</div>
  </article>
  <article class="service-card" style="left:609px">
    <div class="photo" role="img" aria-label="Provider reviewing results with a patient" style="background:linear-gradient(135deg,#b7a995,#5d5247)"></div>
    <div class="icon-badge"><svg width="20" height="20" viewBox="0 0 20 20"><circle cx="10" cy="10" r="5" fill="none" stroke="#fff" stroke-width="3"/></svg></div>
    <h3 class="display">Hepatitis C Care</h3>
    <p>Early diagnosis, treatment, and follow-up care to help eliminate Hepatitis C.</p>
    <div class="read-more">Read More</div>
  </article>
  <article class="service-card" style="left:853px">
    <div class="photo" role="img" aria-label="Laptop showing a video consultation" style="background:linear-gradient(135deg,#c4b39e,#6b5a48)"></div>
    <div class="icon-badge"><svg width="20" height="20" viewBox="0 0 20 20"><rect x="3" y="5" width="14" height="9" rx="1" fill="#fff"/><rect x="7" y="15" width="6" height="2" fill="#fff"/></svg></div>
    <h3 class="display">Online Consultation</h3>
    <p>Speak with licensed healthcare professionals securely from your phone or computer.</p>
    <div class="read-more">Read More</div>
  </article>
</section>

<section>
  <div class="pill" style="top:1244px">Trusted Care</div>
  <h2 class="section-title display" style="top:1272px">Your Trusted Telemedicine Healthcare</h2>
  <p class="lead" style="top:1318px">We provide compassionate, confidential, and evidence-based care for HIV prevention, HIV treatment, and Hepatitis C management.<br>Our mission is to make quality healthcare accessible, affordable, and convenient for everyone.</p>
  <div class="photo" role="img" aria-label="Female doctor in a white coat with a stethoscope" style="left:123px;top:1395px;width:408px;height:360px;border-radius:14px;background:linear-gradient(160deg,#ece9e6,#b9c3cc)"></div>
  <div class="abs" style="left:594px;top:1395px;width:2px;height:360px;background:var(--line)"></div>
  <div class="abs" style="left:593px;top:1395px;width:4px;height:110px;background:var(--blue)"></div>
  <div class="feature" style="top:1395px"><span class="num display">01</span><h4 class="display">100 Confidential Care</h4><p>Your privacy is our priority. Every consultation and medical record is handled with complete confidentiality and secure technology.</p></div>
  <div class="feature" style="top:1520px"><span class="num display">02</span><h4 class="display">Licensed Medical Professionals</h4><p>Receive expert care from experienced healthcare providers dedicated to delivering safe, evidence-based treatment.</p></div>
  <div class="feature" style="top:1643px"><span class="num display">03</span><h4 class="display">Personalized Treatment Plans</h4><p>Every patient receives individualized care &amp; ongoing support tailored to their unique health needs and goals.</p></div>
</section>

<section>
  <div class="pill" style="top:1860px">How It Works</div>
  <h2 class="section-title display" style="top:1888px">How Our Telemedicine Process Works</h2>
  <div class="abs process-panel"></div>
  <div class="photo" role="img" aria-label="Nurse in scrubs taking notes beside a laptop and a potted plant" style="left:60px;top:2010px;width:1080px;height:430px;border-radius:30px;background:linear-gradient(120deg,#d9b9a4,#c59c85 60%,#b48770)"></div>
  <div class="step" style="left:86px"><div class="n display">01</div><div class="t display">Book Your Appointment</div></div>
  <div class="divider" style="left:343px"></div>
  <div class="step" style="left:343px"><div class="n display">02</div><div class="t display">Meet Your Provider Online</div></div>
  <div class="divider" style="left:600px"></div>
  <div class="step" style="left:600px"><div class="n display">03</div><div class="t display">Receive Your Personalized</div></div>
  <div class="divider" style="left:855px"></div>
  <div class="step" style="left:855px"><div class="n display">04</div><div class="t display">Ongoing FollowUp Care</div></div>
</section>

<section>
  <div class="pill" style="top:2708px">Why Choose Us</div>
  <h2 class="section-title display" style="top:2736px">Why Patients Choose Our Clinic</h2>
  <article class="why-card" style="left:123px;width:311px">
    <div class="photo" role="img" aria-label="Doctor and patient talking at a desk" style="background:linear-gradient(135deg,#a9a39a,#e2c98a)"></div>
    <h3 class="display">Confidential And Private Care</h3>
  </article>
  <div class="tick" style="left:259px"><svg width="16" height="16" viewBox="0 0 16 16"><path d="M3 8l3 3 7-7" stroke="#fff" stroke-width="2.2" fill="none"/></svg></div>
  <article class="why-card" style="left:446px;width:308px">
    <div class="photo" role="img" aria-label="Team of medical providers reviewing notes" style="background:linear-gradient(135deg,#e8eaec,#a9b6c2)"></div>
    <h3 class="display">Licensed Medical Providers</h3>
  </article>
  <div class="tick" style="left:581px"><svg width="16" height="16" viewBox="0 0 16 16"><path d="M3 8l3 3 7-7" stroke="#fff" stroke-width="2.2" fill="none"/></svg></div>
  <article class="why-card" style="left:768px;width:307px">
    <div class="photo" role="img" aria-label="Doctor on a virtual consultation call" style="background:linear-gradient(135deg,#6d5a4a,#d8d2ca)"></div>
    <h3 class="display">Secure Virtual Consultations</h3>
  </article>
  <div class="tick" style="left:902px"><svg width="16" height="16" viewBox="0 0 16 16"><path d="M3 8l3 3 7-7" stroke="#fff" stroke-width="2.2" fill="none"/></svg></div>
</section>

<section>
  <div class="pill" style="top:3205px">FAQS</div>
  <h2 class="section-title display" style="top:3233px">Frequently Asked Questions</h2>
  <div class="faq" style="top:3292px;height:112px">
    <h4 class="display">Is my consultation completely confidential and secure?</h4>
    <p>Yes. Your privacy and confidentiality are our highest priorities. All appointments are conducted through a secure telemedicine platform, and your personal information and medical records are protected using strict privacy standards. We are committed to providing a safe, respectful, and judgment-free environment where you can discuss your health concerns with confidence.</p>
    <div class="faq-toggle"><svg width="10" height="10" viewBox="0 0 10 10"><path d="M2 3.5l3 3 3-3" stroke="#fff" stroke-width="1.6" fill="none"/></svg></div>
  </div>
  <div class="faq" style="top:3413px;height:44px"><h4 class="display">Can I receive HIV or Hepatitis C treatment entirely online?</h4><div class="faq-toggle"><svg width="10" height="10" viewBox="0 0 10 10"><path d="M5 2v6M2 5h6" stroke="#fff" stroke-width="1.6"/></svg></div></div>
  <div class="faq" style="top:3466px;height:45px"><h4 class="display">What is PrEP, and who should consider taking it?</h4><div class="faq-toggle"><svg width="10" height="10" viewBox="0 0 10 10"><path d="M5 2v6M2 5h6" stroke="#fff" stroke-width="1.6"/></svg></div></div>
  <div class="faq" style="top:3520px;height:45px"><h4 class="display">How do I book an appointment with your clinic?</h4><div class="faq-toggle"><svg width="10" height="10" viewBox="0 0 10 10"><path d="M5 2v6M2 5h6" stroke="#fff" stroke-width="1.6"/></svg></div></div>
</section>

<section>
  <div class="pill" style="top:3657px">Testimonials</div>
  <h2 class="section-title display" style="top:3685px">What Our Patients Say</h2>
  <svg class="abs" style="left:318px;top:3778px" width="78" height="52" viewBox="0 0 78 52"><path d="M4 30a20 20 0 0 1 22-26v10a12 12 0 0 0-8 10h8v26H4zM44 30a20 20 0 0 1 22-26v10a12 12 0 0 0-8 10h8v26H44z" fill="var(--blue)"/></svg>
  <p class="abs quote">"I was nervous about seeking treatment online, but the entire experience exceeded my expectations. Scheduling my appointment was quick, the virtual consultation was completely private, and the healthcare provider took the time to answer all of my questions. I felt respected, supported, and confident in my treatment plan from the very beginning. I highly recommend this clinic to anyone looking for compassionate and confidential care."</p>
  <div class="abs" style="left:318px;top:4050px;color:#f5a623;font-size:16px;letter-spacing:1px">★★★★★</div>
  <div class="abs display" style="left:327px;top:4074px;font-size:13px">Dana R</div>
  <div class="photo" role="img" aria-label="Smiling woman using a laptop on a sofa" style="left:641px;top:3755px;width:432px;height:360px;border-radius:12px;background:linear-gradient(135deg,#e9e4dd,#b8a793)"></div>
</section>

<footer>
  <div class="abs footer"></div>
  <h2 class="abs display" style="left:94px;top:4270px;font-size:30px;color:var(--white)">Ready to Take Control of Your Health?</h2>
  <p class="abs" style="left:94px;top:4312px;font-size:9px;color:var(--foot-text)">Book a confidential online consultation with our experienced healthcare team today.</p>
  <div class="btn btn-green" style="left:956px;top:4282px;width:110px;height:34px">Book Now</div>
  <div class="arrow-circle" style="left:1068px;top:4281px"><svg width="16" height="16" viewBox="0 0 16 16"><path d="M3 8h10M9 4l4 4-4 4" stroke="#fff" stroke-width="2" fill="none" stroke-linecap="round"/></svg></div>
  <div class="abs" style="left:94px;top:4474px;display:flex;align-items:center;gap:12px;font-family:'Righteous',sans-serif;font-size:30px;color:var(--white)"><span style="width:44px;height:44px;border-radius:50%;background:var(--green)"></span>BRV Online</div>
  <div class="foot-col" style="left:493px"><h5>Quick Links</h5><ul><li>Home</li><li>PrEP</li><li>HIV Treatment</li><li>Hep C</li><li>About</li><li>Contact</li></ul></div>
  <div class="foot-col" style="left:743px"><h5>Services</h5><ul><li>HIV Treatment</li><li>PrEP</li><li>Hepatitis C Care</li><li>Online Consultations</li></ul></div>
  <div class="foot-col" style="left:987px"><h5>Social Media</h5><ul><li>Friendbook</li><li>Snapgram</li><li>WorkLink</li><li>Chirp</li></ul></div>
  <div class="abs" style="left:40px;top:4599px;width:1120px;height:1px;background:#3a3a3a"></div>
  <p class="abs" style="left:0;width:1200px;top:4626px;text-align:center;font-size:9px;color:var(--foot-text)">© 2026 Your Clinic Name. All Rights Reserved.</p>
</footer>

</body>
</html>
```